Tumble Nest - mobile play centre poster designs

Who are we - we are a mobile playground business that specialises in providing entertainment to children in a safe, clean environment either at home or in a function centre. Brief - create 4 different signs to be displayed on our playgrounds. Please find attached 3 photos from our competitors to use as a guide. Corflute sign - size A1 Toddler zone - size A1 Playground rules - size A4 No climbing - size 20cmx8cm sending through photos and documents now.
Colors
Designer to choose colors to be used in the design.
Requirements
Must have
- Colour, be very specific with the rules, pictures

```html
<!DOCTYPE html>
<html lang="en">
<head>
<meta charset="utf-8">
<title>Tumble Nest – Playground Rules</title>
<link href="https://fonts.googleapis.com/css2?family=Montserrat:wght@500;600;700;800&family=Varela+Round&family=Oswald:wght@500&display=swap" rel="stylesheet">
<style>
  :root{
    --bg:#ececec;
    --paper:#ffffff;
    --brand:#e5242b;
    --grey-text:#6d6d6d;
    --blue:#0a6ff0;
    --ink:#151515;
    --ribbon:#ef474b;
    --ribbon-dark:#c1272d;
    --shoes:#e8232a;
    --climb:#1565e0;
    --food:#3f7f2a;
    --bottle:#d4a53a;
    --sharp:#555555;
    --gum:#ee2f7f;
    --face:#e8232a;
    --heels:#6e5a4c;
  }
  html,body{margin:0;padding:0;width:1200px;height:1200px;overflow:hidden;background:var(--bg);}
  .poster{position:absolute;left:365px;top:20px;width:470px;height:1160px;background:var(--paper);font-family:"Montserrat",sans-serif;}
  .brand{position:absolute;left:36px;top:44px;width:400px;}
  .brand-name{font-family:"Montserrat",sans-serif;font-weight:800;font-size:48px;line-height:1;color:var(--brand);letter-spacing:-0.5px;margin:0;}
  .brand-tag{font-weight:600;font-size:21px;color:var(--grey-text);letter-spacing:1px;margin-top:18px;}
  .notice-title{position:absolute;left:0;right:0;top:176px;text-align:center;font-family:"Varela Round",sans-serif;font-weight:700;font-size:37px;color:var(--blue);margin:0;-webkit-text-stroke:0.8px var(--blue);}
  .notice-body{position:absolute;left:30px;right:30px;top:226px;text-align:center;font-weight:600;font-size:16px;line-height:23px;color:var(--ink);margin:0;}
  .art{position:absolute;inset:0;}
  .ribbon-text{position:absolute;left:0;right:0;top:322px;text-align:center;color:#fff;font-weight:700;font-size:20px;letter-spacing:0.5px;}
  .mascot{position:absolute;left:150px;top:392px;width:190px;height:268px;border-radius:46% 46% 30% 30%;background:radial-gradient(ellipse at 50% 45%,#f1c9a0 0 28%,#7a4c2c 60%,#5b3820 100%);}
  .rule{position:absolute;transform:translateX(-50%);text-align:center;font-family:"Oswald",sans-serif;font-weight:500;text-transform:uppercase;line-height:1;letter-spacing:-0.5px;white-space:nowrap;font-size:20px;}
  .rule small{display:block;font-size:9px;letter-spacing:-0.2px;margin-top:1px;}
  .rule.shoes{left:73px;top:614px;color:var(--shoes);}
  .rule.climb{left:393px;top:610px;color:var(--climb);font-size:18px;}
  .rule.climb span{display:block;font-size:14px;}
  .rule.food{left:72px;top:758px;color:var(--food);line-height:22px;}
  .rule.bottle{left:393px;top:756px;color:var(--bottle);line-height:22px;}
  .rule.sharp{left:72px;top:916px;color:var(--sharp);line-height:22px;}
  .rule.gum{left:396px;top:914px;color:var(--gum);font-size:18px;line-height:19px;}
  .rule.face{left:161px;top:1029px;color:var(--face);}
  .rule.heels{left:323px;top:1029px;color:var(--heels);}
  .web{position:absolute;left:46px;top:1087px;width:377px;height:41px;background:var(--blue);color:#fff;font-weight:600;font-size:23px;line-height:41px;text-align:center;letter-spacing:0.3px;}
</style>
</head>
<body>
<main class="poster">
  <header class="brand">
    <h1 class="brand-name">Tumble Nest</h1>
    <div class="brand-tag">MOBILE PLAY CENTRE</div>
  </header>

  <h2 class="notice-title">Parents/Guardians</h2>
  <p class="notice-body">Must supervise children using this play<br>equipment at all times</p>

  <svg class="art" viewBox="0 0 470 1160" width="470" height="1160" aria-hidden="true">
    <polygon points="42,323 82,323 82,368 42,368 55,346" fill="var(--ribbon-dark)"/>
    <polygon points="386,323 426,323 413,346 426,368 386,368" fill="var(--ribbon-dark)"/>
    <polygon points="82,368 121,368 82,360" fill="#8e1b20"/>
    <polygon points="386,368 347,368 386,360" fill="#8e1b20"/>
    <rect x="82" y="311" width="304" height="49" fill="var(--ribbon)"/>

    <g fill="none" stroke-width="2">
      <polyline points="77,540 77,507 210,507" stroke="#f2878b"/>
      <polyline points="392,540 392,508 296,508" stroke="#5aa8f5"/>
      <polyline points="106,710 221,710 221,594" stroke="#5e9e45"/>
      <polyline points="359,710 262,710 262,594" stroke="#e0b24a"/>
      <polyline points="103,852 212,785 212,594" stroke="#666"/>
      <polyline points="369,847 272,785 272,594" stroke="#f55b9b"/>
      <polyline points="173,953 233,874 233,591" stroke="#ee2a2f"/>
      <polyline points="310,951 251,874 251,591" stroke="#6b5446"/>
    </g>
    <g>
      <circle cx="77" cy="507" r="3.5" fill="#f2878b"/>
      <circle cx="392" cy="508" r="3.5" fill="#5aa8f5"/>
      <circle cx="145" cy="710" r="3.5" fill="#5e9e45"/>
      <circle cx="314" cy="710" r="3.5" fill="#e0b24a"/>
      <circle cx="212" cy="785" r="3.5" fill="#666"/>
      <circle cx="272" cy="785" r="3.5" fill="#f55b9b"/>
      <circle cx="233" cy="874" r="3.5" fill="#ee2a2f"/>
      <circle cx="251" cy="874" r="3.5" fill="#6b5446"/>
    </g>

    <defs>
      <g id="no-sign">
        <circle r="34" fill="currentColor" stroke="#e4e4e4" stroke-width="3"/>
        <circle r="22" fill="none" stroke="#fff" stroke-width="3.5"/>
        <line x1="-15.5" y1="15.5" x2="15.5" y2="-15.5" stroke="#fff" stroke-width="3.5"/>
      </g>
    </defs>
    <use href="#no-sign" x="73" y="569" color="#f2878b"/>
    <use href="#no-sign" x="393" y="569" color="#5aa8f5"/>
    <use href="#no-sign" x="71" y="710" color="#5e9e45"/>
    <use href="#no-sign" x="394" y="710" color="#f2c44e"/>
    <use href="#no-sign" x="72" y="869" color="#8a8a8a"/>
    <use href="#no-sign" x="396" y="871" color="#f55b9b"/>
    <use href="#no-sign" x="161" y="983" color="#ee2a2f"/>
    <use href="#no-sign" x="323" y="983" color="#6b5446"/>
  </svg>

  <div class="ribbon-text">PLAY GROUND RULES</div>
  <div class="mascot" role="img" aria-label="Cartoon monkey mascot standing and waving"></div>

  <div class="rule shoes">No Shoes<small>Socks must be worn</small></div>
  <div class="rule climb">No<br>Climbing<span>The Nets</span></div>
  <div class="rule food">No Food<br>Or Drink</div>
  <div class="rule bottle">No Bottle<br>Or Glass</div>
  <div class="rule sharp">No Sharp<br>Objects</div>
  <div class="rule gum">No<br>Chewing<br>Gum</div>
  <div class="rule face">No Face Painting</div>
  <div class="rule heels">No Stilettos</div>

  <div class="web">www.tumblenestplay.com</div>
</main>
</body>
</html>
```